Downloadable PDF "Brochure?"

We have a Free download we will provide in exchange for an email address on our new Trailmark website. The website at www.venturetrailmark-example.com is in development and will look nothing like what it currently does, but you can go there and get a sense of what Trailmark is from the text on the website. (see the attached image 'site design' for the new redesigned website for aesthetics).

We are looking for a nice design for the document, that will represent the mostly text document well. We are not actually looking to print these at a printer so they don't have to be print ready. I went ahead and included the logo and colors and fonts file again just for reference.

Target Market(s)

Business Owners / Decision Makers

Requirements
Must have
• See attached document 'trailmark freebie' for text to be utilized in the finished deliverable.
• See the attached image 'Site Design' for the website aesthetic.

```html
<!DOCTYPE html>
<html lang="en">
<head>
<meta charset="utf-8">
<title>Trailmark – 10 Questions Brochure</title>
<link href="https://fonts.googleapis.com/css2?family=Cinzel:wght@400;700&family=Open+Sans:wght@400;600;700&display=swap" rel="stylesheet">
<style>
:root{
  --bg:#d9d9db;
  --slate:#3f4a52;
  --slate-deep:#333c43;
  --orange:#c8703a;
  --ink:#2c2f33;
  --paper:#ffffff;
  --paper-soft:#f2f3f4;
  --rule:#3f4a52;
}
*{box-sizing:border-box;margin:0;padding:0}
html,body{width:929px;height:1200px;overflow:hidden;background:var(--bg)}
body{position:relative;font-family:"Open Sans",Arial,sans-serif;color:var(--ink)}
.spread{position:absolute;left:52px;width:826px;height:534px;background:var(--paper)}
.spread--outer{top:52px}
.spread--inner{top:614px}
.page{position:absolute;top:0;width:413px;height:100%;overflow:hidden}
.page--left{left:0}
.page--right{left:413px}
.soft{background:linear-gradient(120deg,#ffffff 0%,#eef0f1 55%,#ffffff 100%)}

.q{color:var(--orange);font-weight:700;font-size:7.3px;line-height:9px;margin-bottom:5px}
.q::after{content:"";display:block;width:64px;height:1.5px;background:var(--rule);margin-top:4px}
.a{font-size:6.9px;line-height:8.4px;margin-bottom:8px}

/* outer left */
.qa-top{position:absolute;left:16px;right:18px;top:22px}
.photo{position:absolute}
.photo--ai{left:0;top:196px;width:413px;height:220px;background:linear-gradient(115deg,#6c6f73 0%,#a5a7aa 35%,#e2b85b 52%,#8d9094 70%,#cfd1d3 100%)}
.band-orange{position:absolute;height:2px;background:var(--orange)}
.contact{position:absolute;left:16px;top:440px;right:16px}
.contact h2{font-family:"Cinzel",serif;font-weight:700;font-size:13.5px;letter-spacing:.5px;color:var(--slate)}
.contact h2::after{content:"";display:block;width:64px;height:1.5px;background:var(--rule);margin-top:5px}
.contact .addr,.contact .mail{font-family:"Cinzel",serif;color:var(--orange);font-size:7.2px;line-height:9px;font-weight:700}
.contact .addr{margin-top:13px}
.contact .mail{margin-top:10px}
.contact .web{position:absolute;right:14px;top:63px;width:148px;text-align:right;font-family:"Cinzel",serif;color:var(--orange);font-weight:700;font-size:6.8px;padding-top:6px;border-top:2px solid var(--orange)}

/* outer right / cover */
.photo--desk{left:0;top:0;width:413px;height:432px;background:linear-gradient(160deg,#8f979d 0%,#c4c9cc 40%,#e5e7e8 60%,#8d8f92 100%)}
.cover-rule{position:absolute;left:0;right:0;top:428px;height:3px;background:var(--orange)}
.banner{position:absolute;left:17px;top:0;width:184px;height:460px}
.banner svg{position:absolute;inset:0}
.banner-content{position:absolute;left:0;right:0;top:52px;text-align:center;color:#fff}
.mark{width:26px;height:26px;border-radius:50%;background:var(--orange);margin:0 auto 10px}
.brand{font-family:"Cinzel",serif;font-size:18px;letter-spacing:1px}
.tagline{font-family:"Cinzel",serif;font-size:8px;margin-top:2px}
.banner hr{border:0;height:1.5px;background:#fff;width:154px;margin:0 auto}
.headline{font-family:"Cinzel",serif;font-size:17px;line-height:23px;margin:12px 0 13px}
.sub{font-family:"Cinzel",serif;font-size:9.5px;line-height:13.5px;margin-top:34px}
.phone{position:absolute;right:28px;top:460px;font-family:"Cinzel",serif;font-weight:700;font-size:20px;color:var(--slate)}
.site{position:absolute;right:28px;top:488px;font-family:"Cinzel",serif;font-weight:700;font-size:8px;color:var(--slate)}
.foot{position:absolute;left:0;right:0;bottom:0;height:11px;background:var(--slate)}
.foot::before{content:"";position:absolute;left:0;right:0;top:0;height:2px;background:var(--orange)}

/* inner left */
.hero{position:absolute;left:0;top:0;width:413px;height:166px;background:linear-gradient(100deg,var(--slate-deep) 0%,var(--slate) 60%,#b4b8bb 100%)}
.hero-title{position:absolute;left:22px;top:40px;color:#fff;font-family:"Cinzel",serif}
.hero-title .big{font-size:27px;line-height:30px;font-weight:400}
.hero-title .small{font-size:16px;line-height:19px}
.photo--window{position:absolute;left:262px;top:14px;width:124px;height:124px;border-radius:50%;background:radial-gradient(circle at 50% 55%,#e9eef2 0%,#b9c6cf 60%,#8e989f 100%)}
.hero-base{position:absolute;left:0;top:166px;width:413px;height:10px;background:linear-gradient(#b9bcbe,#e6e7e8)}
.intro{position:absolute;left:16px;right:16px;top:176px}
.intro .a{margin-bottom:12px}
</style>
</head>
<body>

<!-- Outer spread -->
<section class="spread spread--outer">
  <div class="page page--left soft">
    <div class="qa-top">
      <p class="q">What would you do first, if you were selected as our advisor? Can you give me details on what your discovery or on-boarding process includes?</p>
      <p class="a">You are looking to make sure that they don’t stop at the technology. There should be a higher focus on understanding what the company processes are and how the people inside the organization get work done. If they focus only on network, security, and disaster recovery assessments then they do not have a business mindset.</p>
      <p class="q">Can you give me an example of a time you gave a suggestion for a solution and it was not taken? Describe the solution and why it was important to the organization. And why do you think they didn’t implement it?</p>
      <p class="a">When they describe why they think the solution was important do they simply talk about risk reduction or uptime improvements without tying them back to an organizational goal or bottleneck. Being able to demonstrate actual business value is a critical skill for a technology advisor. For reference on technical excellence in service of business objectives rather than blindly servicing requirements see ‘The Shared Table’ by Martin Shale.</p>
    </div>
    <div class="band-orange" style="left:0;right:0;top:194px"></div>
    <div class="photo photo--ai" role="img" aria-label="Robot hand touching a glowing laptop keyboard with AI lettering"></div>
    <div class="band-orange" style="left:0;right:0;top:416px"></div>
    <div class="contact">
      <h2>Contact Us</h2>
      <p class="addr">1200 Meridian Parkway, Suite 200<br>Brookfield, TX 77000</p>
      <p class="mail">hello@venturetrailmark-example.com<br>(555) 014-0580</p>
      <p class="web">www.venturetrailmark-example.com</p>
    </div>
  </div>

  <div class="page page--right">
    <div class="photo photo--desk" role="img" aria-label="Hands writing in a notebook beside a laptop keyboard"></div>
    <div class="cover-rule"></div>
    <div class="banner">
      <svg width="184" height="460" viewBox="0 0 184 460" aria-hidden="true">
        <polygon points="0,0 184,0 184,428 92,460 0,428" fill="#3f4a52" opacity=".96"/>
        <polyline points="12,418 92,438 172,418" fill="none" stroke="#c8703a" stroke-width="2"/>
      </svg>
      <div class="banner-content">
        <div class="mark"></div>
        <div class="brand">TRAILMARK</div>
        <div class="tagline">Discover Your Business Path</div>
        <div style="height:38px"></div>
        <hr>
        <div class="headline">Technology<br>Advisors That<br>"Get" Business.</div>
        <hr>
        <div class="sub">We help you leverage<br>technology to create<br>a competitive advantage</div>
      </div>
    </div>
    <div class="phone">(555) 014-0580</div>
    <div class="site">www.venturetrailmark-example.com</div>
    <div class="foot"></div>
  </div>
</section>

<!-- Inner spread -->
<section class="spread spread--inner">
  <div class="page page--left soft">
    <div class="hero">
      <div class="hero-title">
        <div class="big">10 QUESTIONS</div>
        <div class="small">TO CHOOSE THE BEST<br>TECHNOLOGY ADVISOR</div>
      </div>
      <div class="photo--window" role="img" aria-label="Businessman standing in a round window overlooking a city skyline"></div>
    </div>
    <div class="hero-base"></div>
    <div class="intro">
      <p class="a" style="margin-top:12px">When you choose a technology advisor whether it be a Managed Service Provider, fractional CIO or a full-time CIO you need to make sure that they understand business just as much as they understand technology. Some of the biggest complaints about the IT department are that they just don’t “Get it”. The questions below should help you determine whether or not they have a technology mindset or a business mindset.</p>
      <p class="q">What is scalability? How important is it from a technology perspective on a scale of 1-&gt;10 with 10 being the highest? What all does scalability impact?</p>
      <p class="a">This question is designed to get a reading on the person’s mindset. A typical technology-minded response would be something describing the ability of systems or software to scale by adding additional resources. When working from a business point of view, however, you want to see it defined as the ability for the organization to support increased volume without sacrificing margins. The importance of this concept cannot be overstated and should be a 9 or 10 in terms of ranking. Regarding impact, you want to see not just an understanding of having to spend money two or three times for a different solution to the same problem, but an acknowledgment of the ‘total’ cost, including adoption fatigue, the opportunity cost of change, and the competitive disadvantage it creates. For concepts of business scalability refer to ‘Growing Up’ by Vern Halden.</p>
      <p class="q">Provide an example where you solved a problem without the use of technology.</p>
      <p class="a">Often technology-minded individuals become so wrapped up in the solutions themselves they fail to realize a policy or process change is far more effective and simple than making changes to existing or introducing new technology. Asking for a specific example here should demonstrate the ability to think from a business mindset. For specific examples reference ‘The Ember Project’ by Kell, Baines, and Stafford.</p>
      <p class="q">How do you go about prioritizing solutions in order of importance for implementation / adoption?</p>
      <p class="a">Answers here should include reference to some form of discovery process or a thorough evaluation at the operations level. One of the key skill sets for someone approaching technology from a business point of view is mapping solutions and their respective importance to business outcomes and (often more importantly) eliminating bottlenecks while respecting that some implementations must necessarily come before others to be viable. For reference on the Theory of Constraints see ‘The Target’ by Elias Goldman.</p>
    </div>
    <div class="foot"></div>
  </div>

  <div class="page page--right soft">
    <div class="qa-top" style="top:22px">
      <p class="q">What is Information Technology Debt?</p>
      <p class="a">Stated simply, ‘IT Debt’ is a measurement of the out-of-date, incomplete or yet-to-be-defined technology changes. Debt occurs for a number of reasons, including lack of qualified personnel to implement the needed solutions (or recognize the problem in the first place); historical spending haunting the organization “we spent money on something like this before and look what it got us”; Fire-fighting (addressing issues purely reactively in a downward spiral leaving no time for fixing the real underlying problem); or most commonly, the budget being already allocated to other company endeavors that seem immediately more pressing. By recognizing what IT Debt is, the individual demonstrates an acknowledgment of how impactful it can be when neglected and not brought to the forefront of business planning sessions.</p>
      <p class="q">Provide an example where you argued against implementing a technology solution and why.</p>
      <p class="a">Despite it being seemingly obvious, using ‘outside of budget’ is not a good answer. Business-minded technology advisors should be intimately aware of how well a proposed solution will integrate into the existing company ecosystem (software tools already present, workflow, and processes), if it drives the company toward reducing/eliminating a bottleneck (and thereby creates more leverage), and if it fits the company’s culture. If any of these are a no, the solution should be carefully examined for what it really offers the organization. If yes, the budget should be evaluated as a cost-benefit analysis, not a flat number ‘not to exceed’.</p>
      <p class="q">What is your ideal method for maintaining technology alignment for the company?</p>
      <p class="a">You want to see a specific process envisioned here. At the very least a recommendation to be involved in business planning meetings or retreats, and ideally a standing technology focused meeting with leadership present should be argued for. For technology to be truly in alignment, it must fit the needs of the organization, not the other way around. This needs to come from the top level, and it means a representative must be present in critical business strategy meetings to understand where the company is headed, what operational constraints they are encountering, and what their short-term goals are. For an outline of how this model has been the underlying key to success for several well-known companies reference ‘Good to Greater’ by Jon Callis.</p>
      <p class="q">How do you plan on measuring and monitoring the adoption success of a solution or project?</p>
      <p class="a">Technically minded individuals often look at the point of ‘it’s up and running and it all works’, as where their responsibilities end. Someone with a business mindset should demonstrate that evaluating how well the solution has been adopted into the day to day workflow, and to what degree the solution has increased leverage or operational transparency are the true critical indicators of success. There should be a specific process of follow-up after implementation to flag adoption or workflow issues due to problems such as inadequate training, unforeseen incompatibilities (whether they be process or technology related), or simply resistance to change. These findings can then be brought back to leadership to evaluate how best to improve successful adoption going forward.</p>
      <p class="q">Provide an example where you had to balance customer and employee technology experience with security and compliance.</p>
      <p class="a">A critical role fulfilled by a technology advisor is being able to balance maintaining compliance and sound security practices with as painless of a technology experience as possible. They should be able to weigh the critical importance of protecting the organization from the negative public relations and liability of a security flaw while respecting a solution must be usable to be useful. Look for an example that demonstrates an understanding of both sides and strikes a balance without going to an extreme in either direction.</p>
    </div>
    <div class="foot"></div>
  </div>
</section>

</body>
</html>
```